Restyle corporate identity (+ logo) for a road construction company

We need a new logo and stationary design for our company VELMOR path. VELMOR path® increases the road base strength, while reducing major costs and time of road construction. Attached some examples of the current design.

Our wishes for the new logo:
- Business look
- Style sheet
- Modern

More information: www.velmorpath-example.com
Updates

Target Market(s)

Government

Industry/Entity Type

Construction

Requirements
Must have
• Logo (with road sign) + text

```html
<!DOCTYPE html>
<html lang="en">
<head>
<meta charset="utf-8">
<title>VELMOR path – Business Card</title>
<link href="https://fonts.googleapis.com/css2?family=Questrial&display=swap" rel="stylesheet">
<style>
  :root {
    --brand-green: #add03b;
    --ink-slate: #55596b;
    --paper: #ffffff;
  }
  * { margin: 0; padding: 0; box-sizing: border-box; }
  html, body {
    width: 1200px;
    height: 1001px;
    overflow: hidden;
    background: var(--paper);
    font-family: "Questrial", "Century Gothic", sans-serif;
  }
  .sheet { position: relative; width: 1200px; height: 1001px; }

  /* Front card */
  .card-front {
    position: absolute;
    left: 272px; top: 74px;
    width: 656px; height: 410px;
    background: var(--paper);
  }
  .card-front .wedge { position: absolute; inset: 0; }
  .brand-small {
    position: absolute;
    left: 26px; top: 26px;
    display: flex; align-items: center; gap: 14px;
    color: var(--brand-green);
    font-size: 37px;
    line-height: 1;
    white-space: nowrap;
  }
  .brand-dot {
    width: 80px; height: 80px;
    border-radius: 50%;
    background: var(--brand-green);
    flex: none;
  }
  .brand-small sup, .brand-large sup { font-size: 0.32em; vertical-align: top; position: relative; top: -2px; }

  .contact-block {
    position: absolute;
    right: 26px;
    text-align: right;
    font-size: 22px;
    line-height: 28px;
    color: var(--ink-slate);
    white-space: nowrap;
  }
  .person { top: 66px; }
  .person .name { color: var(--paper); font-size: 29px; line-height: 34px; letter-spacing: 0.5px; }
  .reach { top: 190px; color: var(--paper); }
  .address { top: 303px; line-height: 27px; }

  /* Back card */
  .card-back {
    position: absolute;
    left: 272px; top: 521px;
    width: 656px; height: 410px;
    background: var(--brand-green);
  }
  .brand-large {
    position: absolute;
    left: 32px; top: 133px;
    display: flex; align-items: center; gap: 22px;
    color: var(--paper);
    font-size: 62px;
    line-height: 1;
    white-space: nowrap;
  }
  .brand-large .brand-dot {
    width: 146px; height: 146px;
    background: var(--paper);
  }
</style>
</head>
<body>
<main class="sheet">
  <section class="card-front">
    <svg class="wedge" width="656" height="410" viewBox="0 0 656 410" aria-hidden="true">
      <polygon points="416,0 656,0 656,410 194,410" fill="var(--brand-green)"/>
    </svg>
    <div class="brand-small">
      <span class="brand-dot"></span>
      <span class="brand-name">VELMOR path<sup>®</sup></span>
    </div>
    <div class="contact-block person">
      <p class="name">Jane Doe</p>
      <p>Member of the Board</p>
      <p>Chief Executive Officer</p>
    </div>
    <div class="contact-block reach">
      <p>Tel: +12 345 67 89</p>
      <p>Email: jane@velmorpath.nl</p>
      <p>Site: www.velmorpath.nl</p>
    </div>
    <div class="contact-block address">
      <p>Lindenhof Plein 58</p>
      <p>2511 KX The Hague</p>
      <p>The Netherlands</p>
    </div>
  </section>

  <section class="card-back">
    <div class="brand-large">
      <span class="brand-dot"></span>
      <span class="brand-name">VELMOR path<sup>®</sup></span>
    </div>
  </section>
</main>
</body>
</html>
```